Construction Company Business Card

Business Card Design using new Logo

Contact Information for Business Card

include all company info and website

Requirements
Must have
• Wesley Corman - President
ph. 254-617-0382
Cedar Knoll, TX
wesley@ironmarkframing.com
www.ironmarkframing.com

```html
<!DOCTYPE html>
<html lang="en">
<head>
<meta charset="utf-8">
<title>Ironmark Framing – Business Card</title>
<link href="https://fonts.googleapis.com/css2?family=Montserrat:wght@500&family=Roboto:wght@400;700&display=swap" rel="stylesheet">
<style>
  :root {
    --backdrop: #dcdcd9;
    --card-white: #ffffff;
    --card-grey: #c1c0c5;
    --brand-red: #d42a2c;
    --text-grey: #a3a3a6;
    --rule-grey: #8c8c8c;
    --logo-grey: #b4b4b7;
  }
  * { margin: 0; padding: 0; box-sizing: border-box; }
  html, body { width: 1200px; height: 801px; overflow: hidden; background: var(--backdrop); }
  .stage {
    position: relative; width: 1200px; height: 801px;
    display: flex; align-items: center; justify-content: center; gap: 50px;
  }
  .card {
    width: 525px; height: 300px; position: relative;
    box-shadow: 0 10px 26px rgba(0,0,0,0.14);
  }
  .card-front { background: var(--card-white); }
  .card-back { background: var(--card-grey); display: flex; align-items: center; justify-content: center; }

  .wordmark {
    font-family: "Montserrat", sans-serif; font-weight: 500;
    letter-spacing: 0.08em; text-transform: uppercase;
    display: flex; align-items: center; gap: 10px; white-space: nowrap;
  }
  .wordmark .mark-square { width: 10px; height: 10px; background: var(--brand-red); flex: none; }
  .wordmark-small { position: absolute; left: 36px; top: 142px; font-size: 15px; color: var(--logo-grey); }
  .wordmark-small .mark-square { width: 7px; height: 7px; }
  .wordmark-large { font-size: 34px; color: #ffffff; gap: 16px; }
  .wordmark-large .mark-square { width: 14px; height: 14px; }

  .divider {
    position: absolute; left: 248px; top: 40px; width: 1px; height: 220px;
    background: var(--rule-grey);
  }
  .contact {
    position: absolute; left: 278px; top: 44px;
    font-family: "Roboto", sans-serif; color: var(--text-grey);
  }
  .contact-name { font-weight: 700; font-size: 22px; color: var(--brand-red); line-height: 1.1; }
  .contact-title { font-size: 13px; margin-top: 4px; }
  .contact-row { display: flex; gap: 10px; font-size: 12.5px; line-height: 1.45; }
  .contact-row svg { width: 12px; height: 12px; flex: none; margin-top: 3px; fill: var(--brand-red); }
  .contact-address { margin-top: 18px; }
  .contact-lines { margin-top: 18px; display: flex; flex-direction: column; gap: 3px; }
</style>
</head>
<body>
<main class="stage">
  <section class="card card-front">
    <div class="wordmark wordmark-small"><span class="mark-square"></span>Ironmark Framing</div>
    <div class="divider"></div>
    <div class="contact">
      <p class="contact-name">Wesley Corman</p>
      <p class="contact-title">President</p>
      <div class="contact-row contact-address">
        <svg viewBox="0 0 12 12"><path d="M6 0a4 4 0 0 0-4 4c0 3 4 8 4 8s4-5 4-8a4 4 0 0 0-4-4zm0 5.5A1.5 1.5 0 1 1 6 2.5a1.5 1.5 0 0 1 0 3z"/></svg>
        <p>418 Quarry Ridge<br>Cedar Knoll, TX 78655</p>
      </div>
      <div class="contact-lines">
        <div class="contact-row">
          <svg viewBox="0 0 12 12"><path d="M2.5 0.5l2 2.5-1.2 1.3a7 7 0 0 0 4.4 4.4L9 7.5l2.5 2-1 2C5 11.5 0.5 7 0.5 1.5z"/></svg>
          <p>254-617-0382</p>
        </div>
        <div class="contact-row">
          <svg viewBox="0 0 12 12"><path d="M0 2h12v8H0zM1 3l5 4 5-4"/><path d="M1 3l5 4 5-4" fill="none" stroke="#fff" stroke-width="1"/></svg>
          <p>wesley@ironmarkframing.com</p>
        </div>
        <div class="contact-row">
          <svg viewBox="0 0 12 12"><circle cx="6" cy="6" r="5.5"/><path d="M0.5 6h11M6 0.5v11M2 3h8M2 9h8" stroke="#fff" stroke-width="0.7" fill="none"/></svg>
          <p>www.ironmarkframing.com</p>
        </div>
      </div>
    </div>
  </section>
  <section class="card card-back">
    <div class="wordmark wordmark-large"><span class="mark-square"></span>Ironmark Framing</div>
  </section>
</main>
</body>
</html>
```